Business Cards for a law firm

Business cards for our law firm. Use our silhoette logo and OAK HARBOR - check our website (www.oakharbor-legal.com)

Contact Information for Business Card

our silhouette logo, OAK HARBOR, 800-555-0147, Dorian Kestrup, dorian@oakharbor-legal.com

Requirements
Must have
• our silhouette logo, OAK HARBOR, 800-555-0147, Dorian Kestrup, dorian@oakharbor-legal.com

```html
<!DOCTYPE html>
<html lang="en">
<head>
<meta charset="utf-8">
<title>Oak Harbor – Business Cards</title>
<link rel="stylesheet" href="https://fonts.googleapis.com/css2?family=Cinzel:wght@600;700&family=Open+Sans:wght@400&display=swap">
<style>
  :root {
    --page-bg: #e9eaee;
    --card-white: #ffffff;
    --navy: #1b2f6a;
    --navy-soft: #273d7e;
    --gold: #f2a516;
    --text-light: #ffffff;
    --brand-font: "Cinzel", serif;
    --body-font: "Open Sans", sans-serif;
  }
  * { box-sizing: border-box; margin: 0; padding: 0; }
  html, body { width: 1200px; height: 874px; overflow: hidden; }
  body { background: var(--page-bg); position: relative; font-family: var(--body-font); }

  .card {
    position: absolute;
    left: 267px;
    width: 665px;
    height: 380px;
    border-radius: 24px;
    overflow: hidden;
    box-shadow: 0 6px 18px rgba(0,0,0,0.18);
  }
  .card--front { top: 40px; background: var(--card-white); }
  .card--back { top: 454px; background: var(--navy); }

  .wordmark {
    position: absolute;
    display: flex;
    align-items: center;
    gap: 16px;
    font-family: var(--brand-font);
    font-weight: 700;
    letter-spacing: 0.12em;
    white-space: nowrap;
  }
  .card--front .wordmark {
    left: 150px; top: 150px;
    font-size: 44px;
    color: var(--navy);
  }
  .wordmark__dot {
    width: 22px; height: 22px; border-radius: 50%;
    background: var(--navy);
    flex: none;
  }

  .figure-area {
    position: absolute;
    left: 40px; top: 40px;
    width: 300px; height: 340px;
    border-radius: 12px 12px 0 0;
    background: linear-gradient(180deg, var(--navy-soft), var(--navy));
  }

  .card--back .wordmark {
    right: 48px; top: 88px;
    font-size: 34px;
    color: var(--text-light);
  }

  .contact-block {
    position: absolute;
    left: 380px; top: 200px;
  }
  .contact-block__name {
    font-family: var(--brand-font);
    font-weight: 700;
    font-size: 25px;
    letter-spacing: 0.04em;
    color: var(--gold);
    white-space: nowrap;
  }
  .contact-block__rule {
    width: 28px; height: 2px; background: var(--gold);
    margin: 10px 0 14px;
  }
  .contact-list { list-style: none; }
  .contact-list li {
    display: flex; align-items: center; gap: 10px;
    font-size: 16px; line-height: 24px;
    color: var(--text-light);
    white-space: nowrap;
  }
  .contact-list svg { width: 14px; height: 14px; flex: none; fill: var(--gold); }
</style>
</head>
<body>

<section class="card card--front" aria-label="Business card front">
  <div class="wordmark"><span class="wordmark__dot"></span>OAK HARBOR</div>
</section>

<section class="card card--back" aria-label="Business card back">
  <div class="figure-area" role="img" aria-label="Large white silhouette figures of the firm's two partners"></div>
  <div class="wordmark">OAK HARBOR</div>

  <div class="contact-block">
    <p class="contact-block__name">Dorian Kestrup</p>
    <div class="contact-block__rule"></div>
    <ul class="contact-list">
      <li>
        <svg viewBox="0 0 24 24" aria-hidden="true"><path d="M6.6 10.8a15 15 0 0 0 6.6 6.6l2.2-2.2c.3-.3.7-.4 1-.2 1.1.4 2.3.6 3.6.6.6 0 1 .4 1 1V20c0 .6-.4 1-1 1A17 17 0 0 1 3 4c0-.6.4-1 1-1h3.5c.6 0 1 .4 1 1 0 1.3.2 2.5.6 3.6.1.3 0 .7-.2 1z"/></svg>
        800-555-0147
      </li>
      <li>
        <svg viewBox="0 0 24 24" aria-hidden="true"><path d="M2 5h20v14H2z M2 5l10 8 10-8" /></svg>
        dorian@oakharbor-legal.com
      </li>
      <li>
        <svg viewBox="0 0 24 24" aria-hidden="true"><circle cx="12" cy="12" r="10"/></svg>
        www.oakharbor-legal.com
      </li>
    </ul>
  </div>
</section>

</body>
</html>
```